Business Card Design

I need a business card designed for my new company BrightOak Home developments I specialise in all aspects of carpentry including Decks, Pergolas, Conventional Framing and fit outs I am open to different colours as long as it fits with my logo.

Industry/Entity Type

Carpentry

Contact Information for Business Card

BrightOak Home Developments, Greg Mollory, 0461802394, specialising in all aspects of carpentry and construction

```html
<!DOCTYPE html>
<html lang="en">
<head>
<meta charset="utf-8">
<title>BrightOak Home Developments – Business Card</title>
<link rel="stylesheet" href="https://fonts.googleapis.com/css2?family=Arimo:wght@400&family=Open+Sans:wght@400&display=swap">
<style>
  :root {
    --card-blue: #0a44f8;
    --text-rust: #c8602a;
    --text-outline: #ffffff;
  }
  html, body {
    margin: 0;
    padding: 0;
    width: 1200px;
    height: 741px;
    overflow: hidden;
    background: var(--card-blue);
  }
  .business-card {
    display: block;
    width: 1200px;
    height: 741px;
  }
  .card-background { fill: var(--card-blue); }
  .card-text {
    fill: var(--text-rust);
    stroke: var(--text-outline);
    paint-order: stroke;
    stroke-linejoin: round;
    text-anchor: middle;
  }
  .company-name, .contact-name, .tagline {
    font-family: "Arimo", Arial, sans-serif;
  }
  .company-name { font-size: 51px; stroke-width: 3.5px; word-spacing: 14px; }
  .contact-name { font-size: 51px; stroke-width: 3.5px; word-spacing: 14px; }
  .contact-phone {
    font-family: "Open Sans", Verdana, sans-serif;
    font-size: 51px;
    stroke-width: 3.5px;
    letter-spacing: 1px;
  }
  .tagline { font-size: 32px; stroke-width: 3px; word-spacing: 14px; }
</style>
</head>
<body>
<svg class="business-card" viewBox="0 0 1200 741" xmlns="http://www.w3.org/2000/svg" role="img" aria-label="BrightOak Home Developments business card">
  <rect class="card-background" x="0" y="0" width="1200" height="741"/>
  <text class="card-text company-name" x="600" y="205">BrightOak Home Developments</text>
  <text class="card-text contact-name" x="600" y="355">Greg Mollory</text>
  <text class="card-text contact-phone" x="600" y="432">0461802394</text>
  <text class="card-text tagline" x="600" y="555">Specialising in all aspects of carpentry and construction</text>
</svg>
</body>
</html>
```